Business Card and Stationery for Brokerage & Consulting Co.
Amber Ridge Associates, Brokerage & Consulting for the Baking Industry
Business Card and Stationery for Brokerage & Consulting Co. - Food
Creative Brief
Professional
Derek Halvorsen
Partner / Business Development
4219 W. Birchmont Ave. Long Beach, CA 90714
derek@amberridgeassociates.com

```html
<!DOCTYPE html>
<html lang="en">
<head>
<meta charset="utf-8">
<title>Amber Ridge Associates — Business Card</title>
<link href="https://fonts.googleapis.com/css2?family=Open+Sans:wght@400;600;700&display=swap" rel="stylesheet">
<style>
  :root {
    --page-bg: #e6e2de;
    --card-top: #ffffff;
    --card-fade: #e4e4e4;
    --maroon: #4a1620;
    --olive: #5f7a35;
    --olive-light: #7b9646;
    --silver: #cfcfcf;
    --white: #ffffff;
    --brand: #4a1620;
  }
  * { margin: 0; padding: 0; box-sizing: border-box; }
  html, body {
    width: 1200px;
    height: 770px;
    overflow: hidden;
    background: var(--page-bg);
    font-family: "Open Sans", Arial, sans-serif;
  }
  .business-card {
    position: absolute;
    left: 50px;
    top: 69px;
    width: 1100px;
    height: 632px;
    border-radius: 42px;
    overflow: hidden;
    background: radial-gradient(ellipse at 50% 25%, var(--card-top) 0%, var(--card-top) 40%, var(--card-fade) 100%);
    box-shadow: 0 10px 30px rgba(0,0,0,0.18);
  }
  .card-waves {
    position: absolute;
    inset: 0;
  }
  .brand-block {
    position: absolute;
    left: 0;
    right: 0;
    top: 30px;
    text-align: center;
  }
  .brand-dot {
    display: block;
    width: 80px;
    height: 80px;
    margin: 0 auto 20px;
    border-radius: 50%;
    background: var(--brand);
  }
  .brand-name {
    font-weight: 600;
    font-size: 40px;
    color: var(--brand);
    letter-spacing: 0.5px;
  }
  .contact-list {
    position: absolute;
    left: 30px;
    top: 440px;
    list-style: none;
    color: var(--white);
    font-size: 20px;
    line-height: 30px;
  }
  .contact-list li {
    display: flex;
    align-items: flex-start;
    gap: 12px;
    margin-bottom: 2px;
  }
  .contact-icon {
    flex: none;
    width: 22px;
    height: 22px;
    margin-top: 4px;
  }
  .person {
    position: absolute;
    right: 40px;
    top: 520px;
    text-align: right;
    color: var(--white);
  }
  .person-name {
    font-weight: 700;
    font-size: 24px;
    line-height: 1.3;
  }
  .person-title {
    font-size: 21px;
    line-height: 1.5;
  }
</style>
</head>
<body>
  <div class="business-card">
    <svg class="card-waves" viewBox="0 0 1100 632" width="1100" height="632" aria-hidden="true">
      <path d="M0,212 C240,275 440,372 650,368 C840,364 980,300 1100,238" fill="none" stroke="var(--silver)" stroke-width="4"/>
      <path d="M0,232 C240,300 440,398 650,392 C850,386 990,315 1100,262 L1100,632 L0,632 Z" fill="var(--maroon)"/>
      <path d="M490,392 C680,405 880,345 1085,240 C1070,270 1050,282 1030,292 C830,378 660,408 490,392 Z" fill="var(--olive)"/>
      <path d="M490,392 C680,405 880,345 1085,240" fill="none" stroke="var(--white)" stroke-width="3"/>
      <path d="M620,402 C800,398 950,345 1060,290 C1040,318 1010,330 990,338 C870,386 740,410 620,402 Z" fill="var(--olive-light)"/>
    </svg>

    <div class="brand-block">
      <span class="brand-dot"></span>
      <div class="brand-name">Amber Ridge Associates</div>
    </div>

    <ul class="contact-list">
      <li>
        <svg class="contact-icon" viewBox="0 0 24 24"><circle cx="12" cy="12" r="12" fill="var(--white)"/><path d="M6,12 L12,6.5 L18,12 L16.5,12 L16.5,17.5 L7.5,17.5 L7.5,12 Z" fill="var(--maroon)"/></svg>
        <span>4219 W. Birchmont Ave. Long Beach,<br>CA 90714</span>
      </li>
      <li>
        <svg class="contact-icon" viewBox="0 0 24 24"><circle cx="12" cy="12" r="12" fill="var(--white)"/><path d="M8.5,6 L11,6 L11.8,9 L10.3,10.2 C11,11.8 12.2,13 13.8,13.7 L15,12.2 L18,13 L18,15.5 C18,16.5 17,17.5 16,17.3 C11,16.6 7.4,13 6.7,8 C6.5,7 7.5,6 8.5,6 Z" fill="var(--maroon)"/></svg>
        <span>310 482-5176</span>
      </li>
      <li>
        <svg class="contact-icon" viewBox="0 0 24 24"><circle cx="12" cy="12" r="12" fill="var(--white)"/><rect x="6" y="8" width="12" height="8.5" fill="var(--maroon)"/><path d="M6,8 L12,13 L18,8" fill="none" stroke="var(--white)" stroke-width="1.2"/></svg>
        <span>derek@amberridgeassociates.com</span>
      </li>
      <li>
        <svg class="contact-icon" viewBox="0 0 24 24"><circle cx="12" cy="12" r="12" fill="var(--white)"/><circle cx="12" cy="12" r="6" fill="none" stroke="var(--maroon)" stroke-width="1.4"/><ellipse cx="12" cy="12" rx="2.6" ry="6" fill="none" stroke="var(--maroon)" stroke-width="1.2"/><line x1="6" y1="12" x2="18" y2="12" stroke="var(--maroon)" stroke-width="1.2"/></svg>
        <span>www.amberridgeassociates.com</span>
      </li>
    </ul>

    <div class="person">
      <div class="person-name">Derek Halvorsen</div>
      <div class="person-title">Partner / Business Development</div>
    </div>
  </div>
</body>
</html>
```